Insurance company needs a business card design

We need a business card design for a Massachusetts-based insurance company Veloria Insurance, LLC. We provide auto insurance to Hispanic (Spanish- or Portuguese-speaking) immigrants in the United States. We will give these business cards to auto dealers where such customers typically go to purchase vehicles. We will provide a solution to the dealers to provide easy insurance to the customers buying cars at their dealerships. Veloria is the Spanish word for protection.
Contact Information for Business Card
Name, Designation, Company Name, Address, Phone Number, Email, Website
Look and feel
Each slider illustrates characteristics of the customer's brand and the style your logo design should communicate.

```html
<!DOCTYPE html>
<html lang="en">
<head>
<meta charset="utf-8">
<title>Veloria Insurance — Business Card</title>
<link href="https://fonts.googleapis.com/css2?family=Raleway:wght@500;600;700;800&family=Roboto:wght@400&display=swap" rel="stylesheet">
<style>
  :root {
    --stage: #222222;
    --navy: #044a7a;
    --orange: #f28a0f;
    --white: #ffffff;
  }
  * { margin: 0; padding: 0; box-sizing: border-box; }
  html, body { width: 1075px; height: 1200px; overflow: hidden; }
  body { background: var(--stage); position: relative; font-family: "Raleway", sans-serif; }

  .card {
    position: absolute;
    left: 206px;
    width: 663px;
    height: 395px;
    box-shadow: 3px 3px 2px rgba(0,0,0,0.6);
    overflow: hidden;
  }
  .card-front { top: 187px; background: var(--white); }
  .card-back { top: 637px; background: var(--navy); }

  .front-band {
    position: absolute; left: 0; right: 0; top: 260px; bottom: 0;
    background: var(--navy);
  }

  .brand {
    position: absolute;
    display: flex; align-items: center;
    font-family: "Raleway", sans-serif;
    font-weight: 800;
    letter-spacing: 1px;
  }
  .brand-dot { border-radius: 50%; background: var(--orange); flex: none; }
  .brand-front {
    top: 40px; right: 42px; width: 250px;
    flex-direction: column; gap: 16px;
    color: var(--navy); font-size: 34px; line-height: 1; text-align: center;
  }
  .brand-front .brand-dot { width: 92px; height: 92px; }
  .brand-back {
    top: 150px; left: 0; right: 0; justify-content: center; gap: 20px;
    color: var(--white); font-size: 40px; line-height: 1;
  }
  .brand-back .brand-dot { width: 96px; height: 96px; }

  .person-name {
    position: absolute; left: 36px; top: 213px;
    color: var(--navy); font-weight: 700; font-size: 26px; line-height: 1;
  }
  .person-title {
    position: absolute; left: 36px; top: 243px;
    color: var(--orange); font-weight: 500; font-size: 16px; line-height: 1;
    font-family: "Roboto", sans-serif;
  }
  .title-rule {
    position: absolute; left: 36px; top: 258px; width: 233px; height: 6px;
    background: var(--orange);
  }

  .contact-list {
    position: absolute; left: 36px; top: 291px;
    list-style: none;
    font-family: "Roboto", sans-serif; font-size: 18px; color: var(--white);
  }
  .contact-list li { display: flex; align-items: center; gap: 6px; height: 23.5px; }
  .contact-list svg { width: 17px; height: 17px; flex: none; }

  .address {
    position: absolute; right: 40px; top: 317px;
    font-family: "Roboto", sans-serif; font-size: 18px; line-height: 23.5px;
    color: var(--white); text-align: right; font-style: normal;
  }
</style>
</head>
<body>
  <section class="card card-front">
    <div class="brand brand-front">
      <span class="brand-dot"></span>
      <span class="brand-name">VELORIA<br>INSURANCE</span>
    </div>

    <h1 class="person-name">DANIEL MARSH</h1>
    <p class="person-title">MANAGING DIRECTOR</p>
    <div class="title-rule"></div>

    <div class="front-band"></div>

    <ul class="contact-list">
      <li>
        <svg viewBox="0 0 24 24" aria-hidden="true"><path fill="#f28a0f" d="M6.6 10.8a15 15 0 0 0 6.6 6.6l2.2-2.2c.3-.3.7-.4 1-.2 1.1.4 2.3.6 3.6.6.6 0 1 .4 1 1V20c0 .6-.4 1-1 1A17 17 0 0 1 3 4c0-.6.4-1 1-1h3.5c.6 0 1 .4 1 1 0 1.3.2 2.5.6 3.6.1.3 0 .7-.2 1z"/></svg>
        <span>044-555 018 274</span>
      </li>
      <li>
        <svg viewBox="0 0 24 24" aria-hidden="true"><rect x="2" y="5" width="20" height="14" fill="#f28a0f"/><path d="M2 5l10 8 10-8" fill="none" stroke="#044a7a" stroke-width="1.6"/></svg>
        <span>hello@veloriaauto.com</span>
      </li>
      <li>
        <svg viewBox="0 0 24 24" aria-hidden="true" fill="none" stroke="#f28a0f" stroke-width="1.8"><circle cx="12" cy="12" r="9.5"/><ellipse cx="12" cy="12" rx="4.2" ry="9.5"/><path d="M2.5 12h19M4 7h16M4 17h16"/></svg>
        <span>www.veloriaauto.com</span>
      </li>
    </ul>

    <address class="address">421, Address line goes here<br>45452,Country Name</address>
  </section>

  <section class="card card-back">
    <div class="brand brand-back">
      <span class="brand-dot"></span>
      <span class="brand-name">VELORIA INSURANCE</span>
    </div>
  </section>
</body>
</html>
```